SPARK - and the compass of quiet days

I´m writing a book about CHANGE and the skills leaders needs to embody the transformation from being amanager to become leaders.
The title of the book in Icelandic is the same as the name of the project (which I want to be used on the designes is:) HAFALDAN
(with the subtitle:) og listin að hlusta

Change is not controlled or managed – Leading effective change is an art form which is one of the big reasons for why 70% of changes within companies fail. The main reason however, is that managers are tasked with managing and directing them. The art form of change is to put it in the hands of leaders who possess the emotional intelligence that is needed – all their other advantages intact – to lead change all the way.

The big problem when it comes to change is that there are too many managers and too few leaders within companies – leaders who possess emotional intelligence which is the most important skill a leader embodies to empower change. A leader has what it takes to empower followership.

A manager tends to push and control, make decisions that he presupposes others to implement the way he expects. An emotionally competent leader leads by example and enhances followership on that journey because of the trust and respect he has earned.

In few words: SOFT SKILLS ARE THE NEW HARD SKILLS!

```html
<!DOCTYPE html>
<html lang="is">
<head>
<meta charset="utf-8">
<title>Hafaldan – og listin að hlusta</title>
<link rel="stylesheet" href="https://fonts.googleapis.com/css2?family=Bebas+Neue&family=Oswald:wght@300;600&display=swap">
<style>
  :root {
    --page-bg: #e6e6e6;
    --cover-black: #050505;
    --title-gold: #e3c33c;
    --text-white: #ffffff;
    --floor-light: #8e96a3;
    --floor-mid: #3c4149;
    --floor-dark: #0b0c0e;
  }
  html, body {
    margin: 0;
    padding: 0;
    width: 1200px;
    height: 800px;
    overflow: hidden;
    background: var(--page-bg);
  }
  .canvas {
    position: relative;
    width: 1200px;
    height: 800px;
  }
  .book-cover {
    position: absolute;
    left: 358px;
    top: 31px;
    width: 484px;
    height: 738px;
    background: var(--cover-black);
    border-radius: 3px;
    overflow: hidden;
  }
  .cover-art {
    position: absolute;
    inset: 0;
    background:
      radial-gradient(ellipse 62% 26% at 68% 62%, var(--floor-light) 0%, var(--floor-mid) 48%, rgba(11,12,14,0) 100%),
      linear-gradient(180deg, var(--cover-black) 0%, var(--cover-black) 36%, var(--floor-dark) 55%, #15171b 70%, var(--cover-black) 100%);
  }
  .book-title {
    position: absolute;
    top: 72px;
    left: 0;
    right: 0;
    margin: 0;
    text-align: center;
    font-family: "Bebas Neue", "Oswald", sans-serif;
    font-weight: 400;
    font-size: 122px;
    line-height: 1;
    letter-spacing: 1px;
    color: var(--title-gold);
  }
  .book-subtitle {
    position: absolute;
    top: 184px;
    left: 0;
    right: 0;
    margin: 0;
    text-align: center;
    font-family: "Oswald", sans-serif;
    font-weight: 300;
    font-size: 33px;
    line-height: 1;
    letter-spacing: 2px;
    text-transform: uppercase;
    color: var(--text-white);
  }
  .book-author {
    position: absolute;
    top: 660px;
    left: 0;
    right: 0;
    margin: 0;
    text-align: center;
    font-family: "Oswald", sans-serif;
    font-weight: 600;
    font-size: 34px;
    line-height: 1;
    letter-spacing: 0.38em;
    text-transform: uppercase;
    color: var(--text-white);
  }
</style>
</head>
<body>
  <main class="canvas">
    <section class="book-cover">
      <div class="cover-art" role="img" aria-label="A single yellow paper boat sailing ahead of a fleet of dark grey paper boats across a spotlit concrete floor"></div>
      <h1 class="book-title">HAFALDAN</h1>
      <p class="book-subtitle">og listin að hlusta</p>
      <p class="book-author">Author Name</p>
    </section>
  </main>
</body>
</html>
```